Harbor Lynx Associates Flyer

Create a tri-fold brochure for Harbor Lynx Associates. I am getting a new logo - waiting on the final file. I've attached the copy.

Target Market(s)

retail energy companies and retail energy brokers

Industry/Entity Type

energy

Font styles to use
Serif

Colors
0054AA
0677BA
7BADD7
CADEEF
E8F1F8

Requirements
Must have
• I will be uploading a picture of myself and my partner - that should be somewhere in the inside.
Nice to have
• follow the color scheme of the logo
Should not have
• no mine pictures -use energy pictures - power lines etc. office picture and picture of 2 businesspeople shaking hands

```html
<!DOCTYPE html>
<html lang="en">
<head>
<meta charset="utf-8">
<title>Harbor Lynx Associates – Tri-fold Brochure</title>
<link rel="stylesheet" href="https://fonts.googleapis.com/css2?family=Lora:ital,wght@0,400;0,500;0,700;1,700&display=swap">
<style>
  :root {
    --backdrop: #e4e4e4;
    --brand-blue: #0054AA;
    --brand-blue-mid: #0677BA;
    --brand-blue-soft: #7BADD7;
    --brand-blue-pale: #CADEEF;
    --brand-blue-mist: #E8F1F8;
    --ink: #0d2440;
    --paper: #ffffff;
    --photo-deep: #06203f;
  }
  * { box-sizing: border-box; margin: 0; padding: 0; }
  html, body { width: 867px; height: 1200px; overflow: hidden; }
  body {
    background: var(--backdrop);
    font-family: "Lora", Georgia, serif;
    position: relative;
  }
  .sheet {
    position: absolute;
    left: 56px;
    width: 755px;
    height: 533px;
    box-shadow: 0 3px 8px rgba(0,0,0,.25);
    overflow: hidden;
  }
  .sheet--outside { top: 49px; background: var(--paper); }
  .sheet--inside { top: 614px; background: var(--photo-deep); }

  /* Outside spread */
  .panel-testimonials {
    position: absolute; left: 0; top: 0; width: 251px; height: 100%;
    background: linear-gradient(90deg, var(--brand-blue) 0%, var(--brand-blue) 78%, #003f80 100%);
    color: var(--paper);
    padding: 103px 0 0 21px;
  }
  .quote { width: 210px; font-size: 8.4px; line-height: 10.8px; }
  .quote p + p { margin-top: 9px; }
  .quote + .quote { margin-top: 20px; }

  .cover-shapes { position: absolute; left: 0; top: 0; width: 755px; height: 533px; }

  .brand-name {
    position: absolute; left: 546px; top: 140px; width: 170px;
    text-align: center; color: var(--ink);
    font-size: 19px; font-weight: 500; line-height: 24px; letter-spacing: .3px;
  }
  .brand-name .brand-dot {
    display: block; width: 34px; height: 34px; margin: 0 auto 8px;
    background: var(--brand-blue); border-radius: 50%;
  }

  .partners-title {
    position: absolute; left: 517px; top: 318px; width: 220px; text-align: center;
    color: var(--brand-blue); font-weight: 700; font-style: italic;
    font-size: 34px; line-height: 43px; letter-spacing: .5px;
  }
  .tagline {
    position: absolute; left: 512px; top: 447px; width: 230px; text-align: center;
    color: var(--ink); font-size: 15px; line-height: 20px;
  }

  .contact-list {
    position: absolute; left: 282px; top: 335px; width: 192px;
    list-style: none; text-align: center; color: var(--ink); font-size: 11.5px;
  }
  .contact-list li { height: 54px; }
  .contact-list .icon {
    display: block; width: 23px; height: 23px; margin: 0 auto 4px;
  }

  /* Inside spread */
  .photo { position: absolute; top: 0; height: 100%; }
  .photo--power-lines { left: 0; width: 251px;
    background: linear-gradient(180deg, #1c4f86 0%, #0b3060 45%, var(--photo-deep) 100%); }
  .photo--partners { left: 251px; width: 252px;
    background: radial-gradient(ellipse at 50% 42%, var(--brand-blue-soft) 0%, var(--brand-blue-mid) 35%, #0a3d78 75%, #082c58 100%); }
  .photo--office { left: 503px; width: 252px;
    background: linear-gradient(180deg, #123e70 0%, #0a2f5c 50%, var(--photo-deep) 100%); }

  .body-copy {
    position: absolute; color: var(--paper);
    font-size: 8.4px; line-height: 10.8px;
  }
  .body-copy--intro { left: 21px; top: 164px; width: 212px; }
  .body-copy--services { left: 21px; top: 283px; width: 212px; }
  .body-copy--recruiting { left: 522px; top: 192px; width: 212px; }
</style>
</head>
<body>

<section class="sheet sheet--outside">
  <aside class="panel-testimonials">
    <div class="quote">
      <p>"Dale Orwin &amp; Harbor Lynx Associates found us the perfect candidate and they did it quickly.  If you're an REP looking for great talent, you should use HLA"</p>
      <p>-Ken Abell, BrightPath Power</p>
    </div>
    <div class="quote">
      <p>"Harbor Lynx Associates helped TPG quickly find a great candidate for an essential position that we need to fill right away".</p>
      <p>-Dana Voss, Tailored Power Group</p>
    </div>
    <div class="quote">
      <p>"Harbor Lynx Associates helped KMT quickly find a great person for our team.  Dale Orwin has more connections than just about anyone else in the industry".</p>
      <p>-Paul Hender, KMT Energy</p>
    </div>
    <div class="quote">
      <p>"Voltmetrix brought on Dale Orwin and Harbor Lynx Associates to help us find an amazing VP of Sales.  Because of Dale's extensive contacts in the retail energy industry, he was able to find the right person for this important role - and he did it quickly".</p>
      <p>-Scott Penner, Voltmetrix</p>
    </div>
  </aside>

  <svg class="cover-shapes" viewBox="0 0 836 591" preserveAspectRatio="none" aria-hidden="true">
    <rect x="278" y="0" width="558" height="591" fill="var(--brand-blue)"/>
    <path d="M278 0 H610 C530 70 455 150 380 238 C340 210 305 185 278 165 Z" fill="var(--ink)"/>
    <path d="M385 236 C470 130 620 45 836 12 V296 H660 C545 296 455 275 385 236 Z" fill="var(--paper)"/>
    <path d="M278 591 C295 470 325 340 375 248 C445 292 530 316 650 318 H836 V591 Z" fill="var(--paper)"/>
  </svg>

  <div class="brand-name"><span class="brand-dot"></span>Harbor Lynx<br>Associates</div>

  <ul class="contact-list">
    <li>
      <svg class="icon" viewBox="0 0 24 24" aria-hidden="true"><rect width="24" height="24" rx="4" fill="var(--brand-blue)"/><path d="M8.5 6.5l2 2-1.3 1.6c.8 1.7 2 2.9 3.7 3.7l1.6-1.3 2 2-1.5 1.8c-3.8-.5-7.3-4-7.8-7.8z" fill="#fff"/></svg>
      555.014.2280
    </li>
    <li>
      <svg class="icon" viewBox="0 0 24 24" aria-hidden="true"><rect width="24" height="24" rx="4" fill="var(--brand-blue)"/><rect x="6" y="8" width="12" height="8.5" rx="1" fill="#fff"/><path d="M6.5 8.5l5.5 4.2 5.5-4.2" fill="none" stroke="var(--brand-blue)" stroke-width="1.2"/></svg>
      dale@harborlynxassociates.com
    </li>
    <li>
      <svg class="icon" viewBox="0 0 24 24" aria-hidden="true"><rect width="24" height="24" rx="4" fill="var(--brand-blue)"/><circle cx="12" cy="12" r="6" fill="none" stroke="#fff" stroke-width="1.5"/><path d="M6 12h12M12 6c-2.5 3-2.5 9 0 12M12 6c2.5 3 2.5 9 0 12" fill="none" stroke="#fff" stroke-width="1.2"/></svg>
      www.harborlynxassociates.com
    </li>
  </ul>

  <h1 class="partners-title">DALE<br>&amp; MARLA</h1>
  <p class="tagline">Retail Energy Recruiting<br>and M&amp;A Consulting</p>
</section>

<section class="sheet sheet--inside">
  <div class="photo photo--power-lines" role="img" aria-label="Photograph: power lines against an evening sky"></div>
  <div class="photo photo--partners" role="img" aria-label="Photograph: portrait of partners Dale and Marla Orwin"></div>
  <div class="photo photo--office" role="img" aria-label="Photograph: modern office interior"></div>

  <p class="body-copy body-copy--intro">Harbor Lynx Associates is the 4th company in the retail energy space started by Dale &amp; Marla Orwin.  Dale &amp; Marla have been in the retail energy space for more than 25 years and are two of the most connected people in the industry.</p>

  <p class="body-copy body-copy--services">Harbor Lynx Associates helps companies in two ways. First, HLA is an experienced M&amp;A consulting firm. Whether you're looking to buy or sell, we can connect you with buyers and sellers that match your target profile. We work with REPs, brokers and retail energy vendors of all types. We're not investment bankers, but we're better connected and charge much less. In the last 12 months, HLA has made the introductions for 3 significant transactions. If now is the right time for a strategic move, we can help.</p>

  <p class="body-copy body-copy--recruiting">Harbor Lynx Associates is also retail energy's most used recruiter.  HLA is the only recruiting company focused exclusively on the retail energy industry.  Since our inception in 2022, HLA has filled over 35 roles - including sales, channel management, pricing, billing, supply, regulatory etc.  Harbor Lynx Associates works quickly and we can find great talent from analyst level positions right up to the most critical C-level jobs.  We help REPs, brokers and retail energy industry vendors find the great people they need to keep growing.  Harbor Lynx Associates only works with experienced retail energy professionals.</p>
</section>

</body>
</html>
```